Vela Errands Web Design Project

Homepage components
o Logo
o Rotating header
o Main menu
o Animation video
o Banners
o Members login
o Latest news

The design’s preferred colors are black (background), silver (main tabs) and white (text)

Site map:
• Home
• News
• About us
o Welcome Note
o Company Profile
• Member Log in
o Registered homepage
? Request a service (form)
? Services directory
? Update profile
? Services history
• Member registration
o Registration form
• Partners
Footer Menu
• Contact us
• Terms & Conditions
• Privacy policy
• Social media links
• Sitemap

Brief about the company:
Vela Errands is a Jordanian company dedicated to elevate and redefine the level of service in the country. We are set out to give premium services at affordable prices. In this fast paced environment that we live in, we barely have the luxury of free time anymore and we, at Vela Errands will be giving you that extra hour or two per day to spend as your heart desires!
By becoming a member you will get access to a world of comfort and peace of mind. We have done the homework on your behalf and have established the network of connections that will enable you to live a headache free life.
We will be providing our members with support and assistance in their day to day lives in the fields that consumes and wastes time the most. We are value driven and below is our “ever-growing” list of services that we will provide at excellent prices:
• Maintenance (carpentry, plumbing, electrical, painting, decorating, gardening… etc)
• Cleaning (pre and post tenancy, periodical deep cleaning, packing and moving services, laundry… etc)
• Personalized delivery services (grocery, important documents, office related supplies, posting cheques, food, paying bills… etc)
• Passport, driving license and ID reissuance
• Travel arrangements (flights, hotels, airport transfers… etc)
• Premium car rental services
• Restaurant reservations
• IT assistance
• Event planning and all related services
• Catering arrangements

Aside from all the services we have on offer we have collaborated with a number of places (that we like to call partners) in town where Vela Errands members are entitled to benefits and privileges that will most certainly add value to their membership. Alongside our partners we have come up with the best formula that will please our members. Below are some of our current partners:

Requirements
Must have
• Homepage components
o Logo
o Rotating header
o Main menu
o Animation video
o Banners
o Members login
o Latest news

```html
<!DOCTYPE html>
<html lang="en">
<head>
<meta charset="utf-8">
<title>Vela Errands</title>
<link href="https://fonts.googleapis.com/css2?family=Open+Sans:ital,wght@0,400;0,600;0,700;1,600;1,700&display=swap" rel="stylesheet">
<style>
:root{
  --page:#3d3d3d;
  --ink:#000;
  --text:#fff;
  --muted:#b5b5b5;
  --dim:#8a8a8a;
  --silver-hi:#e9e9e9;
  --silver-lo:#a9a9a9;
  --rule:#1c1c1c;
  --accent:#f2c200;
}
*{box-sizing:border-box;margin:0;padding:0}
html,body{width:1200px;height:900px;overflow:hidden;background:var(--page);font-family:"Open Sans",Arial,sans-serif;color:var(--text)}
.site{position:absolute;left:285px;top:0;width:630px;height:900px;background:var(--ink)}
.abs{position:absolute}
.brand{left:85px;top:14px}
.brand-name{font-size:30px;font-weight:400;letter-spacing:.5px;color:var(--text)}
.brand-tag{font-size:9px;color:var(--dim);margin-left:20px;margin-top:-4px}
.login{left:350px;top:26px;width:190px;font-size:7px}
.login-title{text-align:right;font-size:7.5px;color:var(--muted);display:flex;justify-content:flex-end;align-items:center;gap:4px}
.login-row{display:flex;gap:5px;margin-top:6px}
.field{width:65px;height:12px;background:#fff;color:#999;font-size:6.5px;padding:1px 4px}
.btn-login{width:50px;height:12px;background:linear-gradient(#777,#3a3a3a);color:#ddd;font-size:7px;text-align:center;line-height:12px;border-radius:2px}
.login-meta{display:flex;justify-content:space-between;margin-top:5px;color:var(--muted);font-size:5.5px}
.login-meta b{color:#fff;font-weight:600}
.nav{left:70px;top:72px;width:490px;height:28px;border-radius:8px 8px 0 0;background:linear-gradient(var(--silver-hi),var(--silver-lo));display:flex;align-items:center;padding-left:17px;gap:0}
.nav a{font-size:7.5px;font-weight:600;color:#333;text-decoration:none;padding:5px 11px}
.nav a.active{background:linear-gradient(#fafafa,#cfcfcf);border-radius:3px}
.social{position:absolute;right:18px;top:10px;display:flex;gap:2px}
.social i{width:7px;height:7px;background:#8e8e8e;display:block}
.hero-band{left:0;top:88px;width:630px;height:191px;background:linear-gradient(90deg,#d6d6d6,#ececec 10%,#ececec 90%,#bdbdbd)}
.hero-photo{left:70px;top:100px;width:490px;height:179px;background:linear-gradient(100deg,#cfd2d1 0%,#b8bdb9 35%,#6f7f70 55%,#3d4a3f 75%,#9a8a72 100%)}
.hero-copy{left:320px;top:140px;width:215px;text-shadow:0 1px 2px rgba(0,0,0,.5)}
.hero-copy h1{font-size:14px;font-weight:700;font-style:italic;line-height:16px}
.hero-copy h2{font-size:10.5px;font-weight:600;font-style:italic;margin-bottom:10px}
.hero-copy p{font-size:5.5px;font-style:italic;line-height:10px}
.btn-read{left:317px;top:224px;width:79px;height:19px;border-radius:10px;background:linear-gradient(#9a9a9a,#5f5f5f);font-size:8.5px;font-weight:600;text-align:center;line-height:19px}
.services{left:85px;top:314px;width:310px;display:grid;grid-template-columns:repeat(5,50px);column-gap:13px;row-gap:14px}
.svc{text-align:center}
.svc span{display:flex;align-items:flex-end;justify-content:center;height:20px;font-size:5.5px;color:var(--muted);line-height:8px;margin-bottom:0}
.svc div{width:50px;height:50px;border:2px solid #fff}
.news{left:430px;top:314px;width:115px}
.news h3{font-size:13px;font-weight:400;margin-bottom:12px}
.news-item{font-size:5.5px;line-height:10px;color:var(--muted);margin-bottom:14px}
.news-item b{color:#fff;font-weight:700;display:block}
.news-item .more{color:#fff;font-weight:700;margin-top:8px}
.rule{left:70px;width:490px;height:1px;background:var(--rule)}
.welcome{left:84px;top:531px;width:204px}
.welcome h3,.video h3{font-size:13px;font-weight:400;margin-bottom:14px}
.welcome p{font-size:5.6px;line-height:9px;color:var(--muted);text-align:justify;margin-bottom:9px}
.welcome b{color:#fff}
.btn-more{display:inline-block;margin-top:10px;background:linear-gradient(#777,#3a3a3a);font-size:7px;padding:2px 7px;border-radius:2px}
.video{left:312px;top:531px}
.player{left:313px;top:560px;width:228px;height:130px}
.thumbs{left:318px;top:709px;display:flex;gap:7px;align-items:center}
.thumbs .t{width:40px;height:40px;border:1px solid #fff}
.promo{left:125px;top:780px;width:356px;height:42px;background:linear-gradient(#2a2a2a,#111);border-radius:2px}
.promo-q{left:0;top:4px;background:var(--accent);color:#111;font-size:8px;font-weight:700;padding:2px 6px;transform:rotate(-3deg);transform-origin:left}
.promo-list{left:182px;top:5px;font-size:5px;line-height:11px;color:#ddd}
.promo-name{left:276px;top:6px;font-size:11px;color:#fff}
.promo-btn{left:274px;top:27px;width:80px;height:11px;background:var(--accent);border-radius:6px;color:#111;font-size:6px;font-weight:700;text-align:center;line-height:11px}
.footer{left:86px;top:869px;display:flex;gap:11px;font-size:6px;color:#ddd}
.copy{right:88px;top:869px;font-size:6px;color:var(--dim)}
.copy b{color:#ddd;font-weight:600}
</style>
</head>
<body>
<div class="site">
  <div class="abs brand">
    <div class="brand-name">Vela Errands</div>
    <div class="brand-tag">we make life easier</div>
  </div>

  <form class="abs login">
    <div class="login-title"><svg width="12" height="10" viewBox="0 0 12 10"><circle cx="9" cy="3" r="2.5" fill="none" stroke="#ccc" stroke-width="1.2"/><path d="M7 5 L1 9" stroke="#ccc" stroke-width="1.4"/></svg>Login to your account</div>
    <div class="login-row"><div class="field">User name</div><div class="field">Password</div><div class="btn-login">Login</div></div>
    <div class="login-meta"><span>&#9745; Keep me logged in for two weeks</span><b>Forgot your password?</b></div>
  </form>

  <div class="abs hero-band"></div>
  <div class="abs hero-photo" role="img" aria-label="Bright living room with a white armchair, green cushion and a garden view through glass doors"></div>
  <nav class="abs nav">
    <a class="active">Home</a><a>News</a><a>About Us</a><a>Member Login</a><a>Member Registraton</a>
    <div class="social"><i></i><i></i><i></i><i></i><i></i></div>
  </nav>
  <div class="abs hero-copy">
    <h1>Convergence of Vela Errands</h1>
    <h2>One platform for all your Life Marketing needs</h2>
    <p>Customized, Scalable &amp; Sophisticated solution for Paid Search Marketing, Social Media Marketing &amp; Display Marketing on various Ad Exchanges. Launch campaigns globally with 80% lower operational overheads &amp; at least 30% more efficiencies.</p>
  </div>
  <div class="abs btn-read">Read More</div>

  <div class="abs services">
    <div class="svc"><span>MAINTENANCE</span><div role="img" aria-label="Classic portrait painting" style="background:linear-gradient(#6b5a2e,#3c3220)"></div></div>
    <div class="svc"><span>CLEANING</span><div role="img" aria-label="Gloved hand cleaning a window" style="background:linear-gradient(#d6dde4,#4b6f9a)"></div></div>
    <div class="svc"><span>PERSONALIZED<br>DEIVERY SERVICES</span><div role="img" aria-label="Grocery shelves" style="background:linear-gradient(#b77a2a,#5a3a18)"></div></div>
    <div class="svc"><span>PASPORT</span><div role="img" aria-label="Smiling traveller" style="background:linear-gradient(#7b8d84,#c89a7a)"></div></div>
    <div class="svc"><span>TRAVEL<br>ARRANGEMENTS</span><div role="img" aria-label="Coastline from above" style="background:linear-gradient(#3f8aa0,#1f4f6a)"></div></div>
    <div class="svc"><span>PREMIM CAR<br>RENTAL SERVICES</span><div role="img" aria-label="Row of black cars" style="background:linear-gradient(#b9b9b9,#2c2c2c)"></div></div>
    <div class="svc"><span>RESTAURANT<br>RESERVATIONS</span><div role="img" aria-label="Diners at a restaurant table" style="background:linear-gradient(#a8763e,#5e3a22)"></div></div>
    <div class="svc"><span>IT<br>ASSISTANCE</span><div role="img" aria-label="Support agent with headset" style="background:linear-gradient(#e8e8e0,#8c7a6a)"></div></div>
    <div class="svc"><span>EVENT<br>PLANNING</span><div role="img" aria-label="Stage lit for an event" style="background:linear-gradient(#6a3cc0,#c03a8a)"></div></div>
    <div class="svc"><span>CATERING<br>ARRANGEMENTS</span><div role="img" aria-label="Plated canapés" style="background:linear-gradient(#d88a3a,#5a2a5a)"></div></div>
  </div>

  <aside class="abs news">
    <h3>Latest News</h3>
    <div class="news-item">10 Jun2012 | 25 comments<b>Strategic Consulting and more</b>Strategic consulting capabilities that reveal and solve operational issues .<div class="more">More...</div></div>
    <div class="news-item">10 Jun 2012 | 25 comments<b>Balanced knowledge</b>Balanced knowledge and experience in the government and commercial sectors.<div class="more">More...</div></div>
  </aside>

  <div class="abs rule" style="top:508px"></div>

  <section class="abs welcome">
    <h3>Wellcome to Vela Errands</h3>
    <p>A clearly defined rule or standard, composed of objective factors which leave little or no room for varying interpretation. The purpose of the ‘Perecore Test’ is to produce predictable and consistent results in its application.</p>
    <p>For more than a decade <b>Vela Errands</b> specialists have provided government agencies with the strategic insight and direction they need to establish communication goals that help overcome these challenges. We use client interviews, customer focus groups, market research and other discovery mechanisms to pinpoint communications needs and establish both short- and long-term objectives.</p>
    <p>Based on this foundation, we then develop a detailed, comprehensive plan with recommendations for communicating with internal and external target audiences through a variety of face-to-face, broadcast, print and digital delivery vehicles.</p>
    <span class="btn-more">More</span>
  </section>

  <section class="abs video"><h3>Video</h3></section>
  <svg class="abs player" viewBox="0 0 228 130">
    <rect width="228" height="118" fill="#7a6a58"/>
    <rect width="228" height="118" fill="url(#g)"/>
    <defs><linearGradient id="g" x1="0" y1="0" x2="0" y2="1"><stop offset="0" stop-color="#d8d4cc"/><stop offset=".55" stop-color="#8a7660"/><stop offset="1" stop-color="#4a3a2c"/></linearGradient></defs>
    <title>Hotel suite interior video</title>
    <rect y="118" width="228" height="12" fill="#1a1a1a"/>
    <rect y="117" width="228" height="2" fill="#555"/><rect y="117" width="96" height="2" fill="#c0201a"/>
    <circle cx="96" cy="118" r="2.5" fill="#ddd"/>
    <rect x="8" y="121" width="1.5" height="6" fill="#ccc"/><rect x="11" y="121" width="1.5" height="6" fill="#ccc"/>
    <path d="M24 122h2l3-2v8l-3-2h-2z" fill="#ccc"/><rect x="34" y="123.5" width="14" height="2" fill="#c0201a"/>
    <text x="58" y="126" font-size="4" fill="#aaa" font-family="Open Sans,sans-serif">04:24 / 09:23</text>
    <text x="205" y="126" font-size="4" fill="#aaa" font-family="Open Sans,sans-serif">360p</text>
    <rect x="218" y="121" width="5" height="5" fill="none" stroke="#ccc" stroke-width=".8"/>
  </svg>
  <div class="abs thumbs">
    <svg width="10" height="14" viewBox="0 0 10 14"><path d="M8 1 2 7l6 6" fill="none" stroke="#ccc" stroke-width="2"/></svg>
    <div class="t" role="img" aria-label="Desk with laptop" style="background:linear-gradient(#b9c6d2,#7a8a9a)"></div>
    <div class="t" role="img" aria-label="Blue lounge chairs" style="background:linear-gradient(#dfe6f2,#3a5ab0)"></div>
    <div class="t" role="img" aria-label="Bright atrium" style="background:linear-gradient(#f2f5f8,#7a9ac0)"></div>
    <div class="t" role="img" aria-label="Tablet on a table" style="background:linear-gradient(#3a2a4a,#9a7ac0)"></div>
    <svg width="10" height="14" viewBox="0 0 10 14"><path d="M2 1l6 6-6 6" fill="none" stroke="#ccc" stroke-width="2"/></svg>
  </div>

  <div class="abs rule" style="top:762px"></div>

  <div class="abs promo">
    <div class="abs promo-q">Are your files private &amp; secure?</div>
    <div class="abs" style="left:6px;top:20px;font-size:6.5px;line-height:8px;color:#fff">Financial data, Passwords,<br>Photos, Personal info etc...</div>
    <div class="abs" role="img" aria-label="Software box" style="left:145px;top:5px;width:24px;height:33px;background:linear-gradient(#c9a23a,#2a2a2a)"></div>
    <div class="abs promo-list">&#128274; Advanced Encryption software<br>&#128274; Password-protected vault<br>&#128274; Ensure privacy &amp; peace of mind</div>
    <div class="abs promo-name">Keepbox</div>
    <div class="abs promo-btn">Start Download &#187;</div>
  </div>

  <footer>
    <div class="abs footer"><span>Contact us</span><span>Terms &amp; Conditions</span><span>Privacy policy</span><span>Social media links</span><span>Sitemap</span></div>
    <div class="abs copy">© <b>Vela Errands</b> | All rights reserved.</div>
  </footer>
</div>
</body>
</html>
```